2 Page Business Flyer for Finance Business

Need a two page flyer created for a finance business. Lots of text and needs to fit on two pages.

Corporate business/banking look and feel. Not too many large images. Lots of white space, clean design. Attached is color palette and the text contents of the flyer.

```html
<!DOCTYPE html>
<html lang="en">
<head>
<meta charset="utf-8">
<title>Vanilla Options – Two Page Flyer</title>
<link href="https://fonts.googleapis.com/css2?family=Nunito+Sans:wght@300;400;600;800&display=swap" rel="stylesheet">
<style>
  :root {
    --backdrop: #d5d6d8;
    --paper: #ffffff;
    --navy: #2f2c4f;
    --navy-soft: #403c66;
    --teal: #3cbfa8;
    --red: #c9463d;
    --purple: #7a72b5;
    --tan: #d8c08a;
    --mist: #eef0f1;
    --ink: #3a3a48;
    --ink-light: #e6e5ef;
  }
  * { box-sizing: border-box; margin: 0; padding: 0; }
  html, body { width: 1200px; height: 822px; overflow: hidden; }
  body {
    background: var(--backdrop);
    font-family: "Nunito Sans", Arial, sans-serif;
    color: var(--ink);
    position: relative;
  }
  .page {
    position: absolute; top: 87px; width: 503px; height: 647px;
    background: var(--paper); overflow: hidden;
  }
  .page--left { left: 90px; }
  .page--right { left: 633px; }
  .abs { position: absolute; }
  .heading {
    font-size: 16.5px; line-height: 19px; font-weight: 300; color: var(--teal);
  }
  .heading strong { font-weight: 800; }
  .rule { position: absolute; width: 37px; height: 1.5px; background: var(--red); }
  .body {
    font-size: 9.2px; line-height: 12px; font-weight: 400;
  }
  .body p + p { margin-top: 12px; }
  .bullets { list-style: none; }
  .bullets li { position: relative; padding-left: 11px; }
  .bullets li::before {
    content: ""; position: absolute; left: 1px; top: 4.5px;
    width: 3px; height: 3px; border-radius: 50%; background: var(--teal);
  }
  .body .bullets { margin-top: 8px; }

  /* left page */
  .split-band { position: absolute; left: 0; top: 225px; width: 503px; height: 5px; display: flex; }
  .split-band .red { width: 406px; background: var(--red); }
  .split-band .purple { flex: 1; background: var(--purple); }
  .example { position: absolute; left: 0; top: 230px; width: 503px; height: 417px; background: var(--navy); }
  .example .body { color: var(--ink-light); }
  .example-kicker { font-size: 13px; line-height: 16px; color: var(--teal); font-weight: 400; }
  .example-title { font-size: 20.5px; line-height: 24px; color: var(--teal); font-weight: 800; }
  .photo {
    background: linear-gradient(135deg, #b8473f 0%, #d05a4e 55%, #a83a34 100%);
  }
  .block { position: absolute; }

  /* right page */
  .section-title { font-size: 12.5px; line-height: 15px; font-weight: 800; color: var(--teal); }
  .why-panel { position: absolute; left: 258px; top: 0; width: 213px; height: 352px; background: var(--navy); }
  .why-panel .body { color: var(--ink-light); }
  .icon-area { background: var(--navy-soft); border-radius: 4px; }
  .panel-band { position: absolute; left: 258px; top: 347px; width: 213px; height: 5px; display: flex; }
  .panel-band .red { width: 173px; background: var(--red); }
  .panel-band .purple { flex: 1; background: var(--purple); }
  .pricing { position: absolute; left: 0; top: 370px; width: 503px; height: 260px; background: var(--mist); }
  .foot-band { position: absolute; left: 0; top: 630px; width: 503px; height: 17px; display: flex; }
  .foot-band .purple { width: 96px; background: var(--purple); }
  .foot-band .red { flex: 1; background: var(--red); }
</style>
</head>
<body>

<section class="page page--left">
  <h2 class="heading abs" style="left:37px; top:37px; width:230px;">How does a <strong>Vanilla Option</strong> contract work?</h2>
  <span class="rule" style="left:37px; top:89px;"></span>
  <div class="body abs" style="left:37px; top:108px; width:196px;">
    <p>The buyer of a vanilla option receives protection against an adverse movement in the exchange rate while allowing full participation in a beneficial move. At no time is the buyer of a Vanilla Option obligated to exercise the Option and transact the currencies, therefore providing flexibility in cases where the requirement to purchase foreign currency is not certain.</p>
  </div>
  <div class="body abs" style="left:265px; top:77px; width:206px;">
    <p>A buyer of vanilla options is required to pay a premium (like an insurance premium) for the right, but not the obligation, to exchange currency at a predetermined rate on a predetermined date.</p>
    <ul class="bullets">
      <li>Set a protection rate which will be your worst-case scenario at expiry.</li>
      <li>Determine the amount of currency you wish to protect.</li>
      <li>Choose an expiry date for the contract.</li>
      <li>Calculate the premium you are required to pay.</li>
    </ul>
  </div>

  <div class="split-band"><span class="red"></span><span class="purple"></span></div>

  <div class="example">
    <p class="example-kicker abs" style="left:34px; top:24px;">Let’s look at an example:</p>
    <h3 class="example-title abs" style="left:34px; top:40px;">You are in importer.</h3>
    <span class="rule" style="left:34px; top:72px;"></span>
    <div class="body abs" style="left:33px; top:88px; width:202px;">
      <p>Your construction company has bid on a project that if successful, will require you to import materials from the United States to use in construction. You have used todays pricing of materials in calculating your bid and want to protect against an adverse move in the US dollar exchange rate from eroding your margin if your bid is chosen for the project.</p>
      <p>You choose to buy a Vanilla Call which will protect you from a rise in the USD/CAD exchange rate above your protection rate. You choose to buy protection on $500,000 USD, with a protection rate (strike rate) of 1.3300 expiring 3 months from now. You are required to pay a premium which in this case is calculated to be 1.8%, or 11,970 CAD.</p>
      <p>Your bid is successful: If the exchange rate is below your protection rate at expiration, you have no obligation relating to the vanilla call and you are free to buy USD at the cheaper spot rate. If the exchange rate is above your protection rate, your have the right to purchase your USD at the protection rate, and thereby claiming your insurance policy.</p>
    </div>
    <div class="body abs" style="left:261px; top:232px; width:206px;">
      <p>Your bid is not successful: You have no obligation relating to the vanilla option however, if at expiry the exchange rate is above the protection rate, you may exercise your right to buy USD at the lower rate and simultaneous sell USD back at the prevailing spot rate, thereby recouping some or all of the premium paid to buy the option.</p>
      <p>Alternatively, if you find out your bid was not successful with time still left until expiration, you may sell your option back into the market in the case that it still has residual value, which will depend on various market factors.</p>
    </div>
  </div>

  <div class="photo abs" role="img" aria-label="Red-toned photo of a desk with a laptop, coffee cup and financial charts" style="left:274px; top:253px; width:229px; height:164px;"></div>
  <span class="block" style="left:485px; top:247px; width:18px; height:22px; background:var(--tan);"></span>
  <span class="block" style="left:251px; top:385px; width:52px; height:54px; background:var(--purple);"></span>
  <span class="block" style="left:292px; top:370px; width:29px; height:29px; background:var(--teal);"></span>
</section>

<section class="page page--right">
  <h3 class="section-title abs" style="left:34px; top:37px;">Characteristics</h3>
  <ul class="bullets body abs" style="left:34px; top:60px; width:210px;">
    <li>You are looking for a straight-forward hedging solution</li>
    <li>You want to receive full benefit from an appreciation of the currency you are exposed to</li>
    <li>You are comfortable receiving protection at the strike rate of the option</li>
    <li>You are willing to pay the non-refundable premium</li>
  </ul>
  <h3 class="section-title abs" style="left:34px; top:177px;">Advantages</h3>
  <ul class="bullets body abs" style="left:34px; top:197px; width:210px;">
    <li>You hedge your foreign currency exposure at a predefined hedge rate</li>
    <li>You can choose the hedge rate that suits your budget requirements</li>
    <li>Provides the ability to fully participate in a favourable exchange rate move</li>
    <li>You can choose from most major currency pairs to meet your needs</li>
  </ul>
  <h3 class="section-title abs" style="left:34px; top:310px;">Risks</h3>
  <div class="body abs" style="left:34px; top:330px; width:210px;">
    <p>Premium paid is non-refundable and remains your only obligation when buying vanilla options</p>
  </div>

  <div class="why-panel">
    <div class="icon-area abs" role="img" aria-label="Money illustration" style="left:65px; top:33px; width:86px; height:80px;"></div>
    <h2 class="heading abs" style="left:21px; top:127px;">Why use<br><strong>Vanilla Options?</strong></h2>
    <span class="rule" style="left:21px; top:177px;"></span>
    <div class="body abs" style="left:21px; top:196px; width:180px;">
      <p>Vanilla options are often compared to an insurance product. The buyer pays a non-refundable premium for the right, but not the obligation to trade currency in the future at the protection rate of the option. This product allows you to participate in a beneficial move to an unlimited extent, which will be the most advantageous outcome, if the exchange rate moves in your favour enough to more than offset the premium paid for the option.</p>
    </div>
  </div>
  <div class="panel-band"><span class="red"></span><span class="purple"></span></div>

  <div class="pricing">
    <h2 class="heading abs" style="left:35px; top:21px;">What <strong>determines the price</strong> of a Vanilla Option?</h2>
    <span class="rule" style="left:35px; top:53px;"></span>
    <div class="body abs" style="left:34px; top:73px; width:445px;">
      <p>The cost of an option is defined by the premium that is required to be paid in order to enter into the contract. Premiums are calculated using the industry standard formulas based upon the Black Scholes model. The most important variables in the option pricing formulas include the following:</p>
      <ul class="bullets" style="margin-top:6px;">
        <li>The current market Spot Rate.</li>
        <li>Market volatility – the higher the volatility, the higher the premium.</li>
        <li>The Term of the Option – a longer term typically results in a higher premium.</li>
        <li>The Strike Rate – the closer to being ITM the protection rate is, the higher the premium.</li>
        <li>The interest rate differential of the two currencies involved.</li>
        <li>Style – European or American, or whether the option can be exercised prior to expiration</li>
      </ul>
      <p style="margin-top:11px;">An option can either a European (meaning that they can only be exercised on the expiry date), or American (meaning that they can be exercised at any time prior to expiration). We normally deals in European options however, we do offer American options under certain circumstances and when specific delivery terms are agreed upon between us and the customer.</p>
    </div>
  </div>
  <div class="foot-band"><span class="purple"></span><span class="red"></span></div>
</section>

</body>
</html>
```